Hochzeitseinladung
Zielgruppe
Gastronomie - Zielgruppe ist ein Hochzeitspaar, welches bei uns feiert. Wir dürfen Ihre Hochzeitseinladung entwerfen.
Aufgabenstellung
Den Textvorschlag des Brautpaares findet Ihr im Anhang. Das Thema der Hochzeit ist AMORE.
1. Die Hochzeitseinladung darf gerne kreativ gestaltet sein, vielleicht in Form des Moodboard-Bildes im Anhang? Mattes hat braune Haare und Locken und Doreen lange braune Haare. Beide tragen eine Brille.
Das Hochzeitspaar hat noch einen kleinen braunen Zwergpudel 'Fips', vielleicht findet er auch noch Platz auf der Einladungskarte ;-).
2. Als Alternativ-Vorschlag wäre ein klassisches Design auf zB geprägtem Papier toll.
3. Etwas Schlichtes mit einem Neon-Accessoire würde das Hochzeitspaar auch gut finden. Zb brauner Karton mit einem Neonband.

```html
<!DOCTYPE html>
<html lang="de">
<head>
<meta charset="utf-8">
<title>Hochzeitseinladung Doreen und Mattes</title>
<link rel="stylesheet" href="https://fonts.googleapis.com/css2?family=Montserrat:wght@400;500;700&family=Mrs+Saint+Delafield&display=swap">
<style>
  :root {
    --backdrop: #e6e7e5;
    --paper: #f5f5f3;
    --ink: #2b2b2b;
    --ink-soft: #6b6b6b;
    --rule: #7a7a7a;
  }
  * { box-sizing: border-box; margin: 0; padding: 0; }
  html, body { width: 1200px; height: 1200px; overflow: hidden; }
  body {
    background: var(--backdrop);
    font-family: "Montserrat", sans-serif;
    color: var(--ink);
    display: flex;
    justify-content: center;
    align-items: center;
    gap: 80px;
  }
  .card {
    position: relative;
    width: 420px;
    height: 900px;
    background: var(--paper);
    box-shadow: 0 2px 10px rgba(0,0,0,0.08);
  }
  .card__rule {
    position: absolute;
    right: 30px;
    width: 1px;
    background: var(--rule);
  }
  .card__vertical-title {
    position: absolute;
    right: 25px;
    width: 12px;
    font-size: 11px;
    font-weight: 400;
    line-height: 19px;
    text-align: center;
    color: var(--ink);
  }
  .card__vertical-title span { display: block; }
  .card__vertical-title .gap { height: 19px; }

  /* Front */
  .front .card__rule { top: 40px; height: 160px; }
  .front .card__vertical-title { top: 232px; }
  .couple {
    position: absolute;
    left: 54px;
    top: 680px;
  }
  .couple__name {
    font-size: 21px;
    font-weight: 500;
    letter-spacing: 0.24em;
    line-height: 1;
  }
  .couple__and {
    position: relative;
    display: flex;
    align-items: center;
    height: 40px;
    margin-left: -8px;
  }
  .couple__and::before, .couple__and::after {
    content: "";
    display: block;
    height: 1px;
    background: var(--ink-soft);
  }
  .couple__and::before { width: 30px; }
  .couple__and::after { width: 34px; }
  .couple__and-word {
    font-family: "Mrs Saint Delafield", cursive;
    font-size: 30px;
    line-height: 1;
    padding: 0 2px;
    color: var(--ink);
  }
  .front__meta {
    position: absolute;
    left: 54px;
    top: 830px;
    font-size: 8px;
    letter-spacing: 0.22em;
    line-height: 17px;
    color: var(--ink-soft);
  }
  .front__meta .place { text-transform: uppercase; }

  /* Back */
  .back .card__rule { top: 45px; height: 160px; }
  .back .card__vertical-title { top: 236px; }
  .schedule {
    position: absolute;
    left: 50px;
    top: 234px;
    list-style: none;
  }
  .schedule__item { margin-bottom: 39px; }
  .schedule__head {
    font-size: 9px;
    font-weight: 700;
    letter-spacing: 0.16em;
    text-transform: uppercase;
    line-height: 13px;
  }
  .schedule__head .time { font-size: 10px; }
  .schedule__detail {
    font-size: 8.5px;
    font-weight: 400;
    letter-spacing: 0.2em;
    text-transform: uppercase;
    line-height: 20px;
    color: var(--ink);
  }
  .back__note {
    position: absolute;
    left: 50px;
    top: 828px;
    font-size: 8px;
    letter-spacing: 0.2em;
    text-transform: uppercase;
    color: var(--ink);
  }
</style>
</head>
<body>

  <section class="card front" aria-label="Vorderseite der Einladung">
    <div class="card__rule"></div>
    <div class="card__vertical-title" aria-label="Wir heiraten">
      <span>W</span><span>I</span><span>R</span><span class="gap"></span>
      <span>H</span><span>E</span><span>I</span><span>R</span><span>A</span><span>T</span><span>E</span><span>N</span>
    </div>
    <div class="couple">
      <p class="couple__name">DOREEN</p>
      <p class="couple__and"><span class="couple__and-word">und</span></p>
      <p class="couple__name">MATTES</p>
    </div>
    <div class="front__meta">
      <p class="place">Lindau</p>
      <p>Motto amore</p>
    </div>
  </section>

  <section class="card back" aria-label="Rückseite der Einladung">
    <div class="card__rule"></div>
    <div class="card__vertical-title" aria-label="Ablauf">
      <span>A</span><span>B</span><span>L</span><span>A</span><span>U</span><span>F</span>
    </div>
    <ul class="schedule">
      <li class="schedule__item">
        <p class="schedule__head"><span class="time">13.30</span> Uhr Standesamt</p>
        <p class="schedule__detail">Brunnenhof Kloster</p>
      </li>
      <li class="schedule__item">
        <p class="schedule__head"><span class="time">13.45</span> Uhr Trauung</p>
      </li>
      <li class="schedule__item">
        <p class="schedule__head"><span class="time">14.30</span> Uhr Sekt-Empfang</p>
        <p class="schedule__detail">Tastes Good</p>
        <p class="schedule__detail">Lindengasse 7</p>
      </li>
      <li class="schedule__item">
        <p class="schedule__head"><span class="time">16</span> Uhr Pause</p>
      </li>
      <li class="schedule__item">
        <p class="schedule__head"><span class="time">18.30</span> Uhr Empfang Gasthaus</p>
        <p class="schedule__detail">Alter Fuhrmann</p>
        <p class="schedule__detail">Marktplatz 12</p>
      </li>
      <li class="schedule__item">
        <p class="schedule__head">Flying Dinner</p>
        <p class="schedule__detail">Cocktails und Party</p>
      </li>
      <li class="schedule__item">
        <p class="schedule__head">Dresscodes</p>
        <p class="schedule__detail">Day Cocktail</p>
        <p class="schedule__detail">Night Black Tie</p>
      </li>
    </ul>
    <p class="back__note">PS don’t forget your dancing shoes</p>
  </section>

</body>
</html>
```